Carrow Building Partners Website

Need a dynamic corporate website that can be built on with time. We want to get our information out to the world and have a place where customers can submit requests for proposals.

Target Market(s)

Custom home owners and buyers. Architects and Real Estate Agents.

Industry/Entity Type

Construction

Number of Pages Required

3 page

Font styles to use
Serif
Sans Serif

Requirements
Must have
• Company logo, about, company contact information, biography, contact, projects,
• Sleek, modern, clean, attractive design.
• Online form customers can use for filling out a request for project proposal.
• Lk hyperlink.
• Uses www.carrowbuildingpartners.com

```html
<!DOCTYPE html>
<html lang="en">
<head>
<meta charset="utf-8">
<title>Carrow Building Partners</title>
<link href="https://fonts.googleapis.com/css2?family=Jura:wght@600;700&family=Arimo:wght@400&display=swap" rel="stylesheet">
<style>
:root{
  --blue-deep:#15509e;
  --blue-dark:#1b5cab;
  --blue-sky:#27a9e1;
  --blue-light:#4cc0ec;
  --nav-active:#0e4f9b;
  --white:#ffffff;
  --panel:#f5f6f8;
  --heading:#555a60;
  --text:#7a7d82;
  --bullet:#8a8d91;
  --link:#0b4f9c;
  --footer:#0a4f99;
}
*{margin:0;padding:0;box-sizing:border-box}
html,body{width:1200px;height:909px;overflow:hidden}
body{position:relative;background:var(--panel);font-family:"Arimo",Arial,sans-serif}

.hero{position:absolute;left:0;top:0;width:1200px;height:608px;overflow:hidden}
.hero-left,.hero-right{position:absolute;inset:0}
.hero-right{background:linear-gradient(160deg,var(--blue-light) 0%,var(--blue-sky) 45%,#1e8fd4 100%)}
.hero-left{background:linear-gradient(180deg,var(--blue-dark) 0%,var(--blue-deep) 100%);clip-path:polygon(0 0,542px 0,669px 608px,0 608px)}

.brand{position:absolute;left:86px;top:58px;font-family:"Jura",sans-serif;font-weight:700;font-size:21px;color:var(--white);letter-spacing:.3px;white-space:nowrap}
.hero-name{position:absolute;left:0;width:1200px;top:290px;text-align:center;font-family:"Jura",sans-serif;font-weight:700;font-size:30px;color:var(--white);letter-spacing:1px}

.nav{position:absolute;top:64px;left:0;list-style:none}
.nav li{position:absolute;white-space:nowrap;font-family:"Jura",sans-serif;font-weight:700;font-size:14.5px;color:var(--white)}
.nav .active{color:var(--nav-active)}
.search{position:absolute;left:1067px;top:48px;width:48px;height:48px;border:2px solid var(--white);border-radius:50%}
.search svg{position:absolute;left:15px;top:15px}

.info{position:absolute;top:0;left:0}
.col{position:absolute;top:641px}
.col h3{font-family:"Jura",sans-serif;font-weight:700;font-size:18px;color:var(--heading);letter-spacing:.3px;white-space:nowrap}
.col ul{list-style:none;margin-top:17px}
.col li{font-size:12.5px;line-height:16px;color:var(--text);height:28.3px;padding-left:19px;position:relative;white-space:nowrap}
.col li::before{content:"»";position:absolute;left:0;top:0;font-size:12px;color:var(--bullet)}
.about p{margin-top:15px;width:520px;font-size:12.5px;line-height:24px;color:var(--text)}
.read-more{display:inline-block;margin-top:17px;margin-left:2px;font-family:"Jura",sans-serif;font-weight:700;font-size:13px;color:var(--link);text-decoration:underline}

.footer{position:absolute;left:0;top:849px;width:1200px;height:60px;background:var(--footer)}
.footer .copy{position:absolute;left:87px;top:22px;font-size:12.5px;color:var(--white);white-space:nowrap}
.social{position:absolute;top:12px;left:0;list-style:none}
.social li{position:absolute;top:0;width:37px;height:37px;border:2px solid var(--white);border-radius:50%;display:flex;align-items:center;justify-content:center;font-family:"Jura",sans-serif;font-weight:700;font-size:12px;color:var(--white)}
</style>
</head>
<body>

<header class="hero">
  <div class="hero-right" role="img" aria-label="City skyline with hard hat and spirit level, tinted light blue"></div>
  <div class="hero-left" role="img" aria-label="Hands cutting timber with a power tool, tinted deep blue"></div>
  <div class="brand">Carrow Building Partners</div>
  <ul class="nav">
    <li class="active" style="left:603px">HOME</li>
    <li style="left:688px">ABOUT</li>
    <li style="left:780px">BIO</li>
    <li style="left:848px">PROJECTS</li>
    <li style="left:964px">CONTACT US</li>
  </ul>
  <div class="search">
    <svg width="14" height="14" viewBox="0 0 14 14"><circle cx="5.8" cy="5.8" r="4.3" fill="none" stroke="#fff" stroke-width="2"/><line x1="9" y1="9" x2="12.5" y2="12.5" stroke="#fff" stroke-width="2.2" stroke-linecap="round"/></svg>
  </div>
  <div class="hero-name">Carrow Building Partners</div>
</header>

<section class="info">
  <div class="col" style="left:86px">
    <h3>PROJECTS</h3>
    <ul><li>New construction</li><li>Renovations</li><li>Site works</li></ul>
  </div>
  <div class="col" style="left:250px">
    <h3>PROFILE</h3>
    <ul><li>Team</li><li>Process</li><li>Testimonials</li><li>History</li></ul>
  </div>
  <div class="col" style="left:404px">
    <h3>CONNECT</h3>
    <ul><li>Home</li><li>About</li><li>Bio</li><li>Projects</li><li>Contact us</li></ul>
  </div>
  <div class="col about" style="left:577px">
    <h3>COMMERCIAL, RESIDENTIAL AND COMMUNITY SOLUTIONS</h3>
    <p>Sed ut perspiciatis unde omnis iste natus error sit voluptatem accusantium doloremque laudan tium, totam rem aperiam, eaque ipsa quae ab illo inventore veritatis et quasi architecto beatae vit ae dicta sunt explicabo. Nemo enim ipsam voluptatem quia voluptas sit aspernatur aut dolores eos qui ratione voluptatem sequi nesciunt.</p>
    <a class="read-more">READ MORE INFO</a>
  </div>
</section>

<footer class="footer">
  <div class="copy">© 2016 Copyrights.Carrow Building Partners.All Rights Reserved.</div>
  <ul class="social">
    <li style="left:907px" aria-label="Social link">Nd</li>
    <li style="left:950px" aria-label="Social link">Ch</li>
    <li style="left:992px" aria-label="Social link">Pk</li>
    <li style="left:1035px" aria-label="Professional network link">Lk</li>
    <li style="left:1078px" aria-label="Video channel link">Vu</li>
  </ul>
</footer>

</body>
</html>
```